Zielgruppe
Wir sind ein Hotelunternehmen und eröffnen einen neuen Standort mit einem Boutique-Hotel. Die Zielgruppe sind Hotelgäste.
Aufgabenstellung
Wir benötigen ein Plakat mit den Maßen 6x4 m (siehe Bild anbei) für unsseren neuen Standort.
Farben Schwarz Weiss
Das Haus wird noch komplett weiß eingekleidet für die spätere Enthüllung und dann kommt das Plakat drüber
TEXT:
Großes Logo Hotel
Wir machen Lustenau noch schöner
Hier entsteht unser Boutique Hotel
Aus der Firmengruppe der Tarvolenz (als Logo)
Bild von Lena Grubhofer mit dem untertext: Lena Grubhofer, Geschäftsführerin Business Hotel Grubhofer

```html
<!DOCTYPE html>
<html lang="de">
<head>
<meta charset="utf-8">
<title>Grubhofer Boutique Hotel – Bauplakat</title>
<link href="https://fonts.googleapis.com/css2?family=Montserrat:wght@600;700&family=Oswald:wght@400;500;600&display=swap" rel="stylesheet">
<style>
  :root {
    --ink: #050507;
    --paper: #ffffff;
    --backdrop: #e6e6e6;
    --brand-green: #1f8f3c;
    --photo-light: #d9d9d9;
    --photo-dark: #4a4a4a;
  }
  * { margin: 0; padding: 0; box-sizing: border-box; }
  html, body {
    width: 1200px; height: 1200px; overflow: hidden;
    background: var(--backdrop);
  }
  .poster {
    position: absolute; left: 0; top: 200px;
    width: 1200px; height: 800px;
    background: var(--paper);
    overflow: hidden;
  }
  .poster-shapes { position: absolute; inset: 0; }
  .hotel-logo {
    position: absolute; left: 63px; top: 80px; width: 530px;
    text-align: center; color: var(--ink);
  }
  .hotel-logo__name {
    font-family: "Montserrat", sans-serif; font-weight: 700;
    font-size: 88px; line-height: 1; letter-spacing: 0.01em;
    white-space: nowrap;
  }
  .hotel-logo__type {
    margin-top: 30px; padding-left: 70px;
    font-family: "Montserrat", sans-serif; font-weight: 600;
    font-size: 30px; letter-spacing: 0.2em; line-height: 1;
    white-space: nowrap;
  }
  .intro {
    position: absolute; left: 60px; top: 330px; width: 540px;
    color: var(--paper); font-family: "Oswald", sans-serif;
  }
  .intro__name {
    font-weight: 600; font-size: 72px; line-height: 1;
    letter-spacing: 0.005em; text-transform: uppercase;
    white-space: nowrap;
  }
  .intro__role {
    margin-top: 30px; font-weight: 400; font-size: 24px;
    line-height: 1.2; text-transform: uppercase; white-space: nowrap;
  }
  .intro__points { list-style: none; margin-top: 18px; }
  .intro__points li {
    font-weight: 400; font-size: 31px; line-height: 48px;
    white-space: nowrap;
  }
  .intro__points li::before {
    content: "\2605"; font-size: 18px; margin-right: 10px;
    vertical-align: 6px;
  }
  .group-mark {
    position: absolute; left: 383px; top: 708px;
    font-family: "Oswald", sans-serif; font-weight: 600;
    font-size: 46px; line-height: 1; color: var(--brand-green);
  }
</style>
</head>
<body>
  <main class="poster">
    <svg class="poster-shapes" width="1200" height="800" viewBox="0 0 1200 800">
      <defs>
        <linearGradient id="portrait-tone" x1="0" y1="0" x2="0" y2="1">
          <stop offset="0" stop-color="var(--photo-dark)"/>
          <stop offset="0.35" stop-color="var(--photo-light)"/>
          <stop offset="1" stop-color="#bcbcbc"/>
        </linearGradient>
      </defs>
      <rect class="band" x="0" y="307" width="1203" height="296" fill="var(--ink)"/>
      <path class="band-curve" d="M0 600 H354 V605 A196 196 0 0 1 158 800 H0 Z" fill="var(--ink)"/>
      <rect class="portrait" role="img" aria-label="Porträtfoto von Lena Grubhofer, Geschäftsführerin, in weißer Bluse, Hand an der Hüfte"
            x="606" y="50" width="528" height="750" rx="40" fill="url(#portrait-tone)"/>
    </svg>

    <header class="hotel-logo">
      <div class="hotel-logo__name">Grubhofer</div>
      <div class="hotel-logo__type">BOUTIQUE HOTEL</div>
    </header>

    <section class="intro">
      <h1 class="intro__name">Lena Grubhofer</h1>
      <p class="intro__role">Geschäftsführerin Business Hotel Grubhofer</p>
      <ul class="intro__points">
        <li>Wir machen Lustenau noch schöner</li>
        <li>Hier entsteht unser Boutique Hotel</li>
      </ul>
    </section>

    <div class="group-mark">Tarvolenz</div>
  </main>
</body>
</html>
```